Digital Album Cover - Vellorin Tamsuvel Under Copper Skies (Piano & Cello)

Hi
I would like a digital album cover

Title: "Under Copper Skies (Piano & Cello)"
Artist: "Caleb Rourke & The Pell Orsola"

Preview of instrumental song:
https://tunevault-example.net/calebrourkepianist/tamsuvel-under-copper-skies-piano-and-cello

```html
<!DOCTYPE html>
<html lang="en">
<head>
<meta charset="UTF-8">
<title>Under Copper Skies (Piano &amp; Cello) — Caleb Rourke &amp; The Pell Orsola</title>
<link rel="stylesheet" href="https://fonts.googleapis.com/css2?family=Cinzel:wght@400;500&family=Montserrat:wght@700&display=swap">
<style>
  :root {
    --sky-top: #0b0d2c;
    --sky-mid: #13163c;
    --mist: #34345f;
    --gold: #c8862f;
    --gold-glow: rgba(200, 134, 47, 0.32);
  }
  html, body {
    margin: 0;
    padding: 0;
    width: 1200px;
    height: 1200px;
    overflow: hidden;
    background: var(--sky-top);
  }
  .cover {
    position: relative;
    width: 1200px;
    height: 1200px;
    overflow: hidden;
  }
  .night-sky {
    position: absolute;
    inset: 0;
    background:
      radial-gradient(ellipse 700px 320px at 640px 1120px, rgba(90, 86, 140, 0.45), rgba(90, 86, 140, 0) 100%),
      linear-gradient(180deg, var(--sky-top) 0%, var(--sky-mid) 55%, var(--mist) 100%);
  }
  .title {
    position: absolute;
    left: 0;
    right: 0;
    top: 340px;
    margin: 0;
    text-align: center;
    font-family: "Cinzel", serif;
    font-weight: 500;
    color: var(--gold);
    font-size: 128px;
    line-height: 167px;
    letter-spacing: 0.01em;
    white-space: nowrap;
  }
  .title .line { display: block; }
  .subtitle {
    position: absolute;
    left: 0;
    right: 0;
    top: 672px;
    margin: 0;
    text-align: center;
    font-family: "Cinzel", serif;
    font-weight: 400;
    color: var(--gold);
    font-size: 64px;
    line-height: 80px;
    white-space: nowrap;
  }
  .divider {
    position: absolute;
    left: 415px;
    top: 818px;
    width: 380px;
    height: 30px;
  }
  .artist {
    position: absolute;
    left: 0;
    right: 0;
    top: 906px;
    margin: 0;
    text-align: center;
    font-family: "Montserrat", sans-serif;
    font-weight: 700;
    color: var(--gold);
    font-size: 30px;
    letter-spacing: 0.24em;
    line-height: 40px;
    white-space: nowrap;
  }
  .corner-ornament {
    position: absolute;
    top: 935px;
    width: 260px;
    height: 260px;
  }
  .corner-ornament.left {
    left: 0;
    background: radial-gradient(circle 115px at 130px 143px, var(--gold-glow), rgba(200, 134, 47, 0) 100%);
  }
  .corner-ornament.right {
    right: 0;
    background: radial-gradient(circle 115px at 130px 143px, var(--gold-glow), rgba(200, 134, 47, 0) 100%);
  }
</style>
</head>
<body>
  <main class="cover">
    <div class="night-sky" role="img" aria-label="Deep navy night sky scattered with small golden stars, fading into soft purple mist at the bottom"></div>

    <h1 class="title">
      <span class="line">UNDER COPPER</span>
      <span class="line">SKIES</span>
    </h1>
    <p class="subtitle">(PIANO &amp; CELLO)</p>

    <svg class="divider" viewBox="0 0 380 30" aria-hidden="true">
      <line x1="8" y1="15" x2="140" y2="15" stroke="#c8862f" stroke-width="1.5"/>
      <line x1="240" y1="15" x2="372" y2="15" stroke="#c8862f" stroke-width="1.5"/>
      <circle cx="8" cy="15" r="3" fill="#c8862f"/>
      <circle cx="372" cy="15" r="3" fill="#c8862f"/>
      <rect x="142" y="5" width="96" height="20" rx="10" fill="rgba(200,134,47,0.35)" role="img" aria-label="Small gold scroll flourish"/>
    </svg>

    <p class="artist">CALEB ROURKE &amp; THE PELL ORSOLA</p>

    <div class="corner-ornament left" role="img" aria-label="Gold filigree corner ornament"></div>
    <div class="corner-ornament right" role="img" aria-label="Gold filigree corner ornament"></div>
  </main>
</body>
</html>
```